A colourful crystal mystical tapestry

I need an image for my book cover. The title of the book is The Woven Lantern . Below, the subtitle is Along Quiet Rivers. The crystals move from bottom right to one third up the cover and into the middle. Stop below book title. (Book is 9x6). The crystals have to look like a multi-colour tapestry. Real crystals appear like they are gently exploding from the bottom right of the cover. More like movement than rocketships pls. But not a bunch of fragments. More clustered together. The upper cover will be white. They crystals are multi-covered bright - shinning. It can not be a bad AI image. It must be sharp and brilliant - a tapestry of colours. It is a spiritual book so, it needs to feel as such. If another creative idea comes to mind...give it a try.. I am open to something completely different as long as if is a multi-colour adult appealing spiritual unique image- which represents the title well. THANKS in advance.

Target Market(s)

Readers of multi-dimensional stories. ADULTS

Industry/Entity Type

Spirituality. Beautiful interesting intriguing.

Requirements
Nice to have
• It's tapestry, not chaos per say.
Should not have
• Anything crappy space like AI I can easily create. Be unique.

```html
<!DOCTYPE html>
<html lang="en">
<head>
<meta charset="UTF-8">
<title>The Woven Lantern — Book Cover</title>
<link href="https://fonts.googleapis.com/css2?family=Pinyon+Script&family=Jost:wght@400&display=swap" rel="stylesheet">
<style>
  :root {
    --backdrop: #e6e6e6;
    --paper: #f1f0ed;
    --ink-navy: #1c1f4a;
    --ink-dark: #16182a;
    --teal: #1f8f86;
    --green: #6a9a2a;
    --gold: #f2b21c;
    --orange: #ee6a1a;
    --red: #d3202a;
    --crimson: #9c1236;
    --blue: #1d3fb8;
    --violet: #5a2a9a;
  }
  * { margin: 0; padding: 0; box-sizing: border-box; }
  html, body {
    width: 1200px; height: 900px; overflow: hidden;
    background: var(--backdrop);
  }
  .cover {
    position: absolute;
    left: 320px; top: 30px;
    width: 560px; height: 840px;
    background: var(--paper);
    overflow: hidden;
  }
  .title {
    position: absolute;
    left: 0; right: 0; top: 70px;
    font-family: 'Pinyon Script', cursive;
    font-weight: 400;
    font-size: 98px;
    line-height: 1.05;
    color: var(--ink-dark);
  }
  .title-line { display: block; white-space: nowrap; }
  .title-line--first { padding-left: 44px; }
  .title-line--second { padding-left: 118px; margin-top: 4px; }
  .title-word {
    background-clip: text;
    -webkit-background-clip: text;
    color: transparent;
  }
  .title-word--cool {
    background-image: linear-gradient(100deg, var(--green), var(--teal) 45%, var(--ink-navy));
  }
  .title-word--warm {
    background-image: linear-gradient(100deg, var(--gold), var(--orange) 30%, var(--red) 60%, var(--crimson) 85%, var(--ink-dark));
  }
  .title-word--deep {
    background-image: linear-gradient(100deg, var(--blue), var(--teal) 18%, var(--ink-dark) 40%, var(--ink-dark));
  }
  .subtitle {
    position: absolute;
    left: 0; right: 0; top: 330px;
    text-align: center;
    padding-left: 36px;
    font-family: 'Jost', sans-serif;
    font-weight: 400;
    font-size: 30px;
    letter-spacing: 0.09em;
    color: var(--ink-navy);
    text-transform: uppercase;
  }
  .crystal-field {
    position: absolute;
    left: 0; top: 0;
    width: 560px; height: 840px;
  }
</style>
</head>
<body>
  <main class="cover">
    <svg class="crystal-field" viewBox="0 0 560 840" role="img" aria-label="Illustration of a rainbow cluster of shining crystals bursting from the lower right of the cover">
      <defs>
        <linearGradient id="spectrum" x1="0" y1="0" x2="1" y2="0">
          <stop offset="0" stop-color="#2a3fc4"/>
          <stop offset="0.22" stop-color="#1fa6b8"/>
          <stop offset="0.42" stop-color="#f4c21e"/>
          <stop offset="0.6" stop-color="#f08a1a"/>
          <stop offset="0.78" stop-color="#d42a1c"/>
          <stop offset="1" stop-color="#a8183a"/>
        </linearGradient>
        <radialGradient id="depth" cx="0.72" cy="0.95" r="0.6">
          <stop offset="0" stop-color="#2b1468" stop-opacity="0.95"/>
          <stop offset="0.55" stop-color="#5a2a9a" stop-opacity="0.75"/>
          <stop offset="1" stop-color="#5a2a9a" stop-opacity="0"/>
        </radialGradient>
      </defs>
      <path d="M20 580 C60 520 110 500 150 490 C200 470 250 430 300 420 C340 405 380 395 420 405 C470 410 520 425 560 440 L560 840 L250 840 C180 800 110 760 60 700 C30 660 10 620 20 580 Z" fill="url(#spectrum)"/>
      <path d="M20 580 C60 520 110 500 150 490 C200 470 250 430 300 420 C340 405 380 395 420 405 C470 410 520 425 560 440 L560 840 L250 840 C180 800 110 760 60 700 C30 660 10 620 20 580 Z" fill="url(#depth)"/>
    </svg>

    <h1 class="title">
      <span class="title-line title-line--first"><span class="title-word title-word--cool">The</span> <span class="title-word title-word--warm">Woven</span></span>
      <span class="title-line title-line--second"><span class="title-word title-word--deep">Lantern</span></span>
    </h1>
    <p class="subtitle">Along Quiet Rivers</p>
  </main>
</body>
</html>
```